VORTIQ Business Card Design

We need a business card for a new company based on the Gold Coast, we are a new supplement distributing company called VORTIQ Sports Nutrition - Bold Horizon Sports Nutrition. We are providing new science based bodybuilding and fitness supplementation. Our company has a key focus towards next generation. We are wanting a card that is cool, innovative and fresh. We would like to see the implementation of the below image in a fresh and very innovative design that stands out. The final design should communicate New, Innovative, Cool, Science and researched based.
Target Market(s)
The target market is fitness and bodybuilder enthusiasts. Young audience so very cool looking.
Industry/Entity Type
Fitness
Contact Information for Business Card
(front of card)
VORTIQ Sports Nutrition.
Milo Harrow
CEO/Sport Nutrition Specialist
0473 628 904
Milo@vortiqfuelworks.example
www.vortiqfuelworks.example
(back of card)
Scientifically formulated supplement range
Private Nutrition consultations
comprehensive sports nutrition seminars
Requirements
Nice to have
- The card could have a cut out on one of the sides or one of the corners rounded off so the card looks different from a normal business card.
Should not have
- The colours need to complement each other and pop out.

```html
<!DOCTYPE html>
<html lang="en">
<head>
<meta charset="utf-8">
<title>VORTIQ Sports Nutrition – Business Cards</title>
<link rel="stylesheet" href="https://fonts.googleapis.com/css2?family=Montserrat:ital,wght@0,400;0,600;0,800;1,700&family=Oswald:wght@500;700&family=Roboto+Slab:wght@900&display=swap">
<style>
  :root {
    --page: #ffffff;
    --card-deep: #0b1c29;
    --card-mid: #17364a;
    --accent: #3aa8e6;
    --accent-soft: #7fc6ef;
    --ink: #ffffff;
    --ink-muted: #c9d3da;
    --rule: #3b5a6e;
    --stamp: #b6bcc1;
  }
  * { box-sizing: border-box; margin: 0; padding: 0; }
  html, body { width: 1200px; height: 494px; overflow: hidden; background: var(--page); }
  .sheet { position: relative; width: 1200px; height: 494px; font-family: "Montserrat", sans-serif; }

  .card {
    position: absolute;
    width: 382px; height: 220px;
    border-radius: 34px 0 0 0;
    background: radial-gradient(ellipse at 50% 45%, var(--card-mid) 0%, var(--card-deep) 75%);
    color: var(--ink);
  }
  .card--a { left: 24px;  top: 16px; }
  .card--b { left: 423px; top: 16px; }
  .card--c { left: 24px;  top: 249px; }
  .card--d { left: 423px; top: 251px; }

  .brand {
    position: absolute; left: 38px; top: 62px;
    display: flex; flex-direction: column; align-items: center; gap: 10px;
    width: 120px;
  }
  .brand__dot { width: 44px; height: 44px; border-radius: 50%; background: var(--accent); }
  .brand__name { font-weight: 800; font-size: 25px; letter-spacing: 1px; color: var(--ink); }

  .person { position: absolute; left: 208px; top: 34px; }
  .person__name { font-size: 14px; color: var(--accent); text-transform: uppercase; letter-spacing: .3px; }
  .person__name b { font-weight: 800; }
  .person__role { font-size: 7.5px; color: var(--ink-muted); margin-top: 3px; }

  .contact {
    position: absolute; left: 202px; top: 121px;
    border-left: 1px solid var(--rule);
    padding-left: 6px;
    list-style: none;
    font-size: 8.5px; line-height: 13px; color: var(--ink-muted);
  }
  .contact li { display: flex; align-items: center; gap: 6px; }
  .contact li:first-child { font-weight: 600; color: var(--ink); }
  .contact svg { width: 8px; height: 8px; fill: var(--accent-soft); flex: none; }

  .tagline {
    position: absolute; font-style: italic; font-weight: 700; font-size: 11.5px;
    text-transform: uppercase; letter-spacing: .2px;
  }
  .tagline__lead { color: var(--accent); }
  .tagline--row { left: 0; right: 0; top: 172px; text-align: center; }
  .tagline--stack { left: 38px; top: 152px; line-height: 14px; }
  .tagline--stack span { display: block; }

  .back {
    position: absolute; left: 830px; top: 132px;
    width: 342px; height: 196px;
    background: radial-gradient(ellipse at 50% 45%, var(--card-mid) 0%, var(--card-deep) 80%);
    transform: rotate(-3.5deg);
    padding: 34px 20px 0 22px;
    color: var(--stamp);
    font-family: "Oswald", sans-serif; font-weight: 700;
    text-transform: uppercase; line-height: .98;
  }
  .back p { white-space: nowrap; }
  .back__l1 { font-size: 33px; letter-spacing: .5px; }
  .back__l2 { font-size: 15.5px; font-weight: 500; }
  .back__l3 { font-family: "Roboto Slab", serif; font-size: 44px; font-weight: 900; letter-spacing: 2px; }
  .back__l4 { font-size: 18px; }
  .back__l5 { font-size: 21px; }
  .back__l6 { font-size: 23px; font-weight: 500; }
</style>
</head>
<body>
<main class="sheet">

  <svg width="0" height="0" style="position:absolute" aria-hidden="true">
    <defs>
      <symbol id="icon-phone" viewBox="0 0 10 10"><path d="M2 0.5l1.6 2.2-.9 1.1c.6 1.2 1.4 2 2.6 2.6l1.1-.9L8.6 7 7.8 9c-3.6-.4-6.4-3.2-6.8-6.8z"/></symbol>
      <symbol id="icon-mail" viewBox="0 0 10 10"><path d="M0 2h10v6H0zM.8 2.6L5 5.6l4.2-3z" fill-rule="evenodd"/></symbol>
      <symbol id="icon-web" viewBox="0 0 10 10"><path d="M5 0a5 5 0 110 10A5 5 0 015 0zm0 1.2a3.8 3.8 0 100 7.6 3.8 3.8 0 000-7.6zM1.5 4.5h7v1h-7z"/></symbol>
    </defs>
  </svg>

  <section class="card card--a">
    <div class="brand"><span class="brand__dot"></span><span class="brand__name">VORTIQ</span></div>
    <div class="person">
      <p class="person__name"><b>Milo</b> Harrow</p>
      <p class="person__role">CEO/Sport Nutrition Specialist</p>
    </div>
    <ul class="contact">
      <li><svg><use href="#icon-phone"/></svg>0473-628-904</li>
      <li><svg><use href="#icon-mail"/></svg>Milo@vortiqfuelworks.example</li>
      <li><svg><use href="#icon-web"/></svg>www.vortiqfuelworks.example</li>
    </ul>
    <p class="tagline tagline--row"><span class="tagline__lead">Bold Horizon</span> Sports Nutrition</p>
  </section>

  <section class="card card--b">
    <div class="brand"><span class="brand__dot"></span><span class="brand__name">VORTIQ</span></div>
    <div class="person">
      <p class="person__name"><b>Theo</b> Brandt</p>
      <p class="person__role">CEO / Supplement Production Manager</p>
    </div>
    <ul class="contact">
      <li><svg><use href="#icon-phone"/></svg>0481-257-936</li>
      <li><svg><use href="#icon-mail"/></svg>theo@vortiqfuelworks.example</li>
      <li><svg><use href="#icon-web"/></svg>www.vortiqfuelworks.example</li>
    </ul>
    <p class="tagline tagline--row"><span class="tagline__lead">Bold Horizon</span> Sports Nutrition</p>
  </section>

  <section class="card card--c">
    <div class="brand" style="top:42px"><span class="brand__dot"></span><span class="brand__name">VORTIQ</span></div>
    <div class="person">
      <p class="person__name"><b>Milo</b> Harrow</p>
      <p class="person__role">CEO/Sport Nutrition Specialist</p>
    </div>
    <ul class="contact">
      <li><svg><use href="#icon-phone"/></svg>0473-628-904</li>
      <li><svg><use href="#icon-mail"/></svg>Milo@vortiqfuelworks.example</li>
      <li><svg><use href="#icon-web"/></svg>www.vortiqfuelworks.example</li>
    </ul>
    <p class="tagline tagline--stack"><span class="tagline__lead">Bold Horizon</span><span>Sports Nutrition</span></p>
  </section>

  <section class="card card--d">
    <div class="brand" style="top:42px"><span class="brand__dot"></span><span class="brand__name">VORTIQ</span></div>
    <div class="person">
      <p class="person__name"><b>Theo</b> Brandt</p>
      <p class="person__role">CEO / Supplement Production Manager</p>
    </div>
    <ul class="contact">
      <li><svg><use href="#icon-phone"/></svg>0481-257-936</li>
      <li><svg><use href="#icon-mail"/></svg>theo@vortiqfuelworks.example</li>
      <li><svg><use href="#icon-web"/></svg>www.vortiqfuelworks.example</li>
    </ul>
    <p class="tagline tagline--stack"><span class="tagline__lead">Bold Horizon</span><span>Sports Nutrition</span></p>
  </section>

  <section class="back">
    <p class="back__l1">Scientifically</p>
    <p class="back__l2">Formulated Supplement Range</p>
    <p class="back__l3">Private</p>
    <p class="back__l4">Nutrition Consultations</p>
    <p class="back__l5">Comprehensive Sports</p>
    <p class="back__l6">Nutrition Seminars</p>
  </section>

</main>
</body>
</html>
```